Website for Company that serves and supports Investment Banks

We are seeking to have a six page website that provides a basic description of our company's services. Our company provides Financial Models and Investment Memos on an outsourced basis to Small Investment Banks and Investment firms. We do not require a shopping cart. We already have a logo attached.

Target Market(s)

Small, regional investment banks. Small private equity firms.

Industry/Entity Type

Finance And Accounting

Coding

Coded - Design and coding required

Number of Pages Required

5+ page

Requirements
Nice to have
• Please use the logo design to drive how you design the layout for the website

```html
<!DOCTYPE html>
<html lang="en">
<head>
<meta charset="utf-8">
<title>LedgerPointAnalyst.com</title>
<link href="https://fonts.googleapis.com/css2?family=Cinzel:wght@400;700&family=Open+Sans:ital,wght@0,400;0,600;1,400&display=swap" rel="stylesheet">
<style>
:root{
  --navy:#0d3461;
  --navy-deep:#0a2b52;
  --navy-dark:#082544;
  --white:#ffffff;
  --ink:#2b2b2b;
  --muted:#555f6b;
  --grey-tab:#dedfe1;
  --icon-grey:#c9ccd1;
}
*{margin:0;padding:0;box-sizing:border-box}
html,body{width:1200px;height:3180px;overflow:hidden}
body{font-family:"Open Sans",Arial,sans-serif;color:var(--ink);background:var(--white);position:relative}
.serif{font-family:"Cinzel",Georgia,serif}
section,header,footer{position:absolute;left:0;width:1200px}

/* header */
.site-header{top:0;height:115px;background:var(--navy)}
.brand{position:absolute;left:0;top:0;width:466px;height:115px;background:var(--white);border-radius:0 58px 58px 0;display:flex;align-items:center;justify-content:center;gap:12px}
.brand-dot{width:26px;height:26px;border-radius:50%;background:var(--navy)}
.brand-name{font-family:"Cinzel",Georgia,serif;font-size:22px;font-weight:700;color:var(--navy)}
.main-nav{position:absolute;right:48px;top:0;height:115px;display:flex;align-items:center;gap:38px}
.main-nav a{color:var(--white);text-decoration:none;font-size:16px;letter-spacing:.3px}
.main-nav a.active{font-weight:600}

/* hero */
.hero{top:115px;height:563px;overflow:hidden}
.hero-photo{position:absolute;inset:0;background:linear-gradient(100deg,#cfd4d8 0%,#e9ecef 35%,#f3f5f6 60%,#dfe4ea 100%)}
.hero-copy{position:absolute;right:85px;top:165px;text-align:right}
.hero-copy h1{font-family:"Open Sans",Arial,sans-serif;font-weight:400;font-size:48px;color:var(--navy);letter-spacing:-.5px}
.hero-copy p{font-size:19px;color:#1c2533;line-height:29px;margin-top:10px}
.btn-solid{display:inline-block;margin-top:20px;background:var(--navy);color:var(--white);font-family:"Cinzel",Georgia,serif;font-size:21px;padding:14px 26px;border-radius:30px;text-decoration:none}
.slide-arrow{position:absolute;top:268px;width:46px;height:46px;border-radius:50%;background:var(--navy);display:flex;align-items:center;justify-content:center}
.slide-arrow.left{left:16px}.slide-arrow.right{right:16px}

/* about */
.about{top:678px;height:386px;background:var(--navy);color:var(--white);text-align:center}
.about h2{font-family:"Cinzel",Georgia,serif;font-size:40px;margin-top:56px;font-weight:400}
.about .sub{font-family:"Cinzel",Georgia,serif;font-size:15px;letter-spacing:1.5px;margin-top:4px}
.about p{font-style:italic;font-size:13.5px;line-height:25px;width:760px;margin:16px auto 0}
.btn-outline{display:inline-block;margin-top:26px;border:2px solid var(--white);color:var(--white);font-family:"Cinzel",Georgia,serif;font-size:21px;padding:10px 28px;border-radius:30px;text-decoration:none}

/* process */
.process{top:1064px;height:388px;text-align:center}
.process h2{font-family:"Cinzel",Georgia,serif;font-size:40px;color:var(--navy);margin-top:54px;font-weight:400}
.steps{display:flex;justify-content:center;gap:22px;margin-top:28px;list-style:none}
.step{width:124px}
.step-icon{width:124px;height:124px;border-radius:50%;border:2px solid #d6d8dc;padding:8px}
.step-icon svg{width:104px;height:104px;display:block}
.step-label{font-size:14.5px;line-height:20px;margin-top:12px;color:#222}

/* products */
.products{top:1452px;height:615px;overflow:hidden}
.products-bg{position:absolute;inset:0;background:linear-gradient(90deg,#cbced3 0%,#d8dadd 45%,#e4e5e7 100%)}
.products h2{position:absolute;top:50px;width:100%;text-align:center;font-family:"Cinzel",Georgia,serif;font-size:40px;color:var(--navy);font-weight:400}
.products .lead{position:absolute;top:110px;left:0;width:100%;text-align:center;font-size:14.5px;line-height:24px;color:#222}
.person{position:absolute;left:700px;top:176px;width:480px;height:439px;background:linear-gradient(180deg,#b9bcc1 0%,#5a5f68 45%,#2d3038 100%);border-radius:200px 200px 0 0}
.price-card{position:absolute;top:214px;width:290px;height:314px;background:var(--white);box-shadow:0 2px 8px rgba(0,0,0,.2)}
.price-card.deal{left:78px}.price-card.value{left:394px}
.price-card h3{height:85px;background:var(--navy);color:var(--white);font-family:"Cinzel",Georgia,serif;font-size:17px;font-weight:400;text-align:center;line-height:26px;padding-top:18px}
.price-row{display:flex;justify-content:space-between;align-items:flex-start;padding:0 14px;margin-top:24px}
.price-row+.price-row{margin-top:22px}
.price-row span{font-size:13px;line-height:20px;color:#333;width:130px}
.price-row b{font-size:19px;color:var(--navy-dark)}

.tabs{top:2067px;height:61px;display:flex}
.tab{flex:1;display:flex;align-items:center;justify-content:center;font-family:"Cinzel",Georgia,serif;font-size:20px;letter-spacing:.5px}
.tab.current{background:var(--navy);color:var(--white);position:relative}
.tab.other{background:var(--grey-tab);color:#222}
.tab-knob{position:absolute;left:265px;top:-28px;width:40px;height:40px;border-radius:50%;background:var(--navy);display:flex;align-items:center;justify-content:center}

/* why */
.why{top:2128px;height:719px;overflow:hidden;background:#f3f6f9}
.why-photo{position:absolute;right:0;top:0;width:620px;height:719px;background:linear-gradient(160deg,#e9eef3 0%,#d7dee6 40%,#c4a98c 75%,#a5886b 100%)}
.why h2{position:absolute;left:78px;top:52px;font-family:"Cinzel",Georgia,serif;font-size:40px;line-height:46px;color:var(--navy);font-weight:400}
.why-list{position:absolute;left:78px;top:162px;width:590px;list-style:none}
.why-list li{position:relative;padding-left:32px;font-size:13.5px;line-height:22px;color:#333;margin-bottom:24px}
.why-list svg{position:absolute;left:0;top:4px}

/* footer */
.site-footer{top:2847px;height:265px;background:var(--navy);color:var(--white)}
.foot-brand{position:absolute;left:78px;top:56px;width:260px;text-align:center}
.foot-brand .brand-dot{margin:0 auto 10px;background:var(--white)}
.foot-brand .name{font-family:"Cinzel",Georgia,serif;font-size:18px;font-weight:700}
.social{display:flex;justify-content:center;gap:14px;margin-top:24px}
.social span{width:46px;height:46px;border-radius:50%;border:2px solid var(--white)}
.social span:first-child{background:var(--white)}
.foot-col{position:absolute;top:34px}
.foot-col h4{font-family:"Cinzel",Georgia,serif;font-size:17px;font-weight:400;letter-spacing:.5px;margin-bottom:18px}
.sitemap{left:345px}
.sitemap ul{list-style:disc;padding-left:22px}
.sitemap li{font-size:13.5px;line-height:29px}
.contact{left:608px}
.contact-row{display:flex;gap:16px;font-size:13.5px;line-height:20px;margin-bottom:18px}
.newsletter{left:876px;width:250px}
.newsletter p{font-size:13.5px;line-height:23px}
.newsletter .field{margin-top:12px;background:var(--white);color:#777;font-size:12.5px;padding:9px 12px;width:250px}
.newsletter .btn-outline{margin-top:14px;font-size:17px;padding:6px 42px}
.copyright{top:3112px;height:68px;background:var(--navy-dark);color:#d8e0ea;font-size:13px;display:flex;align-items:center;justify-content:center}
</style>
</head>
<body>

<header class="site-header">
  <div class="brand"><span class="brand-dot"></span><span class="brand-name">LedgerPointAnalyst.com</span></div>
  <nav class="main-nav">
    <a class="active" href="#">HOME</a><a href="#">ABOUT</a><a href="#">PRODUCT</a><a href="#">WHY HIRE</a><a href="#">PROCESS</a><a href="#">CONTACT</a>
    <svg width="20" height="20" viewBox="0 0 20 20" aria-label="Search"><circle cx="8" cy="8" r="6" fill="none" stroke="#fff" stroke-width="2.6"/><line x1="12.5" y1="12.5" x2="18" y2="18" stroke="#fff" stroke-width="3" stroke-linecap="round"/></svg>
  </nav>
</header>

<section class="hero">
  <div class="hero-photo" role="img" aria-label="Analyst in glasses reviewing papers at a laptop in a bright office"></div>
  <div class="slide-arrow left"><svg width="14" height="18" viewBox="0 0 14 18"><path d="M10 2 L3 9 L10 16" stroke="#fff" stroke-width="2.4" fill="none"/></svg></div>
  <div class="slide-arrow right"><svg width="14" height="18" viewBox="0 0 14 18"><path d="M4 2 L11 9 L4 16" stroke="#fff" stroke-width="2.4" fill="none"/></svg></div>
  <div class="hero-copy">
    <h1>LedgerPointAnalyst.com</h1>
    <p>Financial Models And Investment Memos On An Outsourced Basis To<br>Small Investment Banks And Investment Firms</p>
    <a class="btn-solid" href="#">CONTACT US</a>
  </div>
</section>

<section class="about">
  <h2>ABOUT US</h2>
  <div class="sub">LEDGERPOINTANALYST.COM</div>
  <p>LedgerPointAnalyst.com functions as an outsourced Financial Analyst partner for smaller, regional investment banks, private equity firms, business brokers, and mezzanine loan funds.</p>
  <p style="margin-top:8px">We Focus Exclusively On Lower Middle-Market Clients We believe Financial Models and Investment Memos are two of the most important deal support tools for executing private equity and investment banking transactions...</p>
  <a class="btn-outline" href="#">LEARN MORE</a>
</section>

<section class="process">
  <h2>OUR WORKS PROCESS</h2>
  <ul class="steps">
    <li class="step"><div class="step-icon"><svg viewBox="0 0 104 104"><circle cx="52" cy="52" r="52" fill="#0d3461"/><path d="M34 40 q18-14 36 0 l-4 8 -8-3 0-5 q-6-3-12 0 l0 5 -8 3z" fill="#fff"/><rect x="38" y="52" width="28" height="18" rx="3" fill="#fff"/></svg></div><div class="step-label">Call Us or<br>Email US</div></li>
    <li class="step"><div class="step-icon"><svg viewBox="0 0 104 104"><circle cx="52" cy="52" r="52" fill="#c9ccd1"/><circle cx="52" cy="54" r="24" fill="none" stroke="#0d3461" stroke-width="4"/><text x="52" y="62" text-anchor="middle" font-family="Open Sans,Arial,sans-serif" font-weight="700" font-size="20" fill="#0d3461">24</text></svg></div><div class="step-label">Reach at<br>24 hours</div></li>
    <li class="step"><div class="step-icon"><svg viewBox="0 0 104 104"><circle cx="52" cy="52" r="52" fill="#c9ccd1"/><rect x="30" y="28" width="26" height="44" rx="3" fill="#fff" stroke="#0d3461" stroke-width="3"/><circle cx="64" cy="50" r="8" fill="#0d3461"/><path d="M50 76 q14-22 28 0z" fill="#0d3461"/></svg></div><div class="step-label">Ensure<br>Confidentiality</div></li>
    <li class="step"><div class="step-icon"><svg viewBox="0 0 104 104"><circle cx="52" cy="52" r="52" fill="#c9ccd1"/><rect x="28" y="56" width="48" height="20" fill="#fff" stroke="#0d3461" stroke-width="3"/><circle cx="52" cy="66" r="5" fill="#0d3461"/><path d="M30 48 L44 36 L56 44 L74 28" stroke="#0d3461" stroke-width="4" fill="none"/></svg></div><div class="step-label">Flow-of-<br>Funds</div></li>
    <li class="step"><div class="step-icon"><svg viewBox="0 0 104 104"><circle cx="52" cy="52" r="52" fill="#c9ccd1"/><rect x="28" y="30" width="48" height="36" fill="#fff" stroke="#0d3461" stroke-width="3"/><rect x="38" y="48" width="6" height="12" fill="#0d3461"/><rect x="49" y="42" width="6" height="18" fill="#0d3461"/><rect x="60" y="38" width="6" height="22" fill="#0d3461"/><line x1="52" y1="66" x2="52" y2="78" stroke="#0d3461" stroke-width="3"/></svg></div><div class="step-label">Create Your<br>Financial Model</div></li>
    <li class="step"><div class="step-icon"><svg viewBox="0 0 104 104"><circle cx="52" cy="52" r="52" fill="#c9ccd1"/><rect x="32" y="26" width="40" height="52" fill="#fff" stroke="#0d3461" stroke-width="3"/><rect x="38" y="54" width="6" height="16" fill="#0d3461"/><rect x="49" y="46" width="6" height="24" fill="#0d3461"/><rect x="60" y="38" width="6" height="32" fill="#0d3461"/></svg></div><div class="step-label">Create your<br>Investment Memo</div></li>
    <li class="step"><div class="step-icon"><svg viewBox="0 0 104 104"><circle cx="52" cy="52" r="52" fill="#c9ccd1"/><circle cx="52" cy="52" r="26" fill="none" stroke="#0d3461" stroke-width="4"/><text x="52" y="60" text-anchor="middle" font-family="Open Sans,Arial,sans-serif" font-weight="700" font-size="20" fill="#0d3461">72</text></svg></div><div class="step-label">Send work On<br>72 Hours</div></li>
  </ul>
</section>

<section class="products">
  <div class="products-bg" role="img" aria-label="Soft grey backdrop of financial figures and currency symbols"></div>
  <h2>PRODUCT OFFERING</h2>
  <p class="lead">•We Offer Standard Prices On Financial Models And Investment Memos That Can Be Purchased On A<br>"Product-By-Product" Basis</p>
  <div class="person" role="img" aria-label="Smiling professional holding a laptop and pointing forward"></div>
  <div class="price-card deal">
    <h3>DEAL TRANSACTION<br>MODELS</h3>
    <div class="price-row"><span>LBO, Growth Equity, Recap</span><b>$3,500</b></div>
  </div>
  <div class="price-card value">
    <h3>VALUATION<br>MODELS</h3>
    <div class="price-row"><span>Discounted Cashflow</span><b>$2,500</b></div>
    <div class="price-row"><span>Comparable Company Analysis</span><b>$1,000</b></div>
    <div class="price-row"><span>Private Multiple Analysis</span><b>$1,000</b></div>
  </div>
</section>

<section class="tabs">
  <div class="tab current"><span class="tab-knob"><svg width="16" height="16" viewBox="0 0 16 16"><path d="M3 8 L8 3 L13 8 M3 14 L8 9 L13 14" stroke="#fff" stroke-width="2" fill="none"/></svg></span>FINANCIAL MODELS:</div>
  <div class="tab other">INVESTMENT DOCUMENTS:</div>
</section>

<section class="why">
  <div class="why-photo" role="img" aria-label="Hand holding a printed report with a colourful pie chart"></div>
  <h2>WHY HIRE<br>LEDGERPOINTANALYST.COM?</h2>
  <ul class="why-list">
    <li><svg width="16" height="14" viewBox="0 0 16 14"><path d="M1 7 L6 12 L15 2" stroke="#0d3461" stroke-width="3" fill="none"/></svg>We are much more cost-effective than hiring full-time Analyst pool</li>
    <li><svg width="16" height="14" viewBox="0 0 16 14"><path d="M1 7 L6 12 L15 2" stroke="#0d3461" stroke-width="3" fill="none"/></svg>We give You the ability to purchase Financial Models and Investment Memos on a "product-by-product" on demand basis with standardized prices</li>
    <li><svg width="16" height="14" viewBox="0 0 16 14"><path d="M1 7 L6 12 L15 2" stroke="#0d3461" stroke-width="3" fill="none"/></svg>Cost of our Financial Models and Investment Memos is less expensive than other outsourced deal providers including investment bankers, attorneys, accountants and industry consultants</li>
    <li><svg width="16" height="14" viewBox="0 0 16 14"><path d="M1 7 L6 12 L15 2" stroke="#0d3461" stroke-width="3" fill="none"/></svg>Cost of our Financial Models and Investment Memos is less expensive than Quality of Earnings Analysis reports provided by accounting firms</li>
    <li><svg width="16" height="14" viewBox="0 0 16 14"><path d="M1 7 L6 12 L15 2" stroke="#0d3461" stroke-width="3" fill="none"/></svg>We provide smaller, regional investment banks and private equity firms to outsource a large portion of their back-office in order to focus more time on marketing for new clients, executing deals and industry networking</li>
    <li><svg width="16" height="14" viewBox="0 0 16 14"><path d="M1 7 L6 12 L15 2" stroke="#0d3461" stroke-width="3" fill="none"/></svg>Most Investment Banking Financial Analysts are "temporary two-year hires" which means constant employee turnover and recruitment, interviewing and training new Analysts that rarely stay with the company beyond two years.</li>
  </ul>
</section>

<footer class="site-footer">
  <div class="foot-brand">
    <div class="brand-dot"></div>
    <div class="name">LedgerPointAnalyst.com</div>
    <div class="social"><span></span><span></span><span></span></div>
  </div>
  <div class="foot-col sitemap">
    <h4>SITEMAP</h4>
    <ul><li>Home</li><li>About</li><li>Product</li><li>Why Hire Process</li><li>Contact</li></ul>
  </div>
  <div class="foot-col contact">
    <h4>CONTACT US</h4>
    <div class="contact-row"><svg width="18" height="24" viewBox="0 0 18 24"><path d="M9 1 a8 8 0 0 1 8 8 c0 6-8 14-8 14 s-8-8-8-14 a8 8 0 0 1 8-8z" fill="#fff"/><circle cx="9" cy="9" r="3" fill="#0d3461"/></svg><span>LedgerPointAnalyst.com<br>410 Harbor Row<br>Suite 12-208<br>Easton, MA 02356</span></div>
    <div class="contact-row"><svg width="18" height="18" viewBox="0 0 18 18"><path d="M3 1 l4 0 1 4 -2 2 q2 4 5 5 l2-2 4 1 0 4 q-1 2-3 2 q-13-2-14-14 q0-2 3-2z" fill="#fff"/></svg><span>555-014-2870</span></div>
    <div class="contact-row"><svg width="18" height="14" viewBox="0 0 18 14"><rect x="0" y="0" width="18" height="14" fill="#fff"/><path d="M0 0 L9 8 L18 0" stroke="#0d3461" stroke-width="1.6" fill="none"/></svg><span>hello@ledgerpointanalyst.com</span></div>
  </div>
  <div class="foot-col newsletter">
    <h4>NEWSLETTER</h4>
    <p>Would you like to receive exclusive access to articles, white papers and our regular monthly newsletter?</p>
    <div class="field">Enter Email *</div>
    <a class="btn-outline" href="#">SUBSCRIBE</a>
  </div>
</footer>
<div class="copyright" style="position:absolute;left:0;width:1200px">©LedgerPointAnalyst.com - 2017 All Right Reserved.</div>

</body>
</html>
```